Design an engaging, visually attractive and well laid out Word Press website

I have a partially completed Word Press website that I need to have completed . The previous designer overestimated her ability to produce a quality product and underestimated my knowledge of how a good well designed website should look visually and be laid out.

A visitor to the site should have a clear understanding of the services offered by the business, be able to navigate the site with ease via effective logical pathways, have calls to action that are prominent and located in the correct locations that prompt the viewer to make contact when they are ready to act. The site needs to be visually impactful, have lots of white space, fast loading and mobile compatible and the visitor needs to have the impression that they need to look no further for the services offered.

I am particularly interested in how you think the Services and Projects pages should be best laid out so they present well on a mobile device without looking cluttered and can be navigated and viewed with ease.

I have the copy and images (these may need some changes) and I have put together a basic version of a layout on MS Word documents. These are all in a Dropbox folder (link below). I am open to a designer offering his/her own thoughts on how the site can be laid out better. Also I have a link below to the partially created website. I will need the website coded once I am happy with the design.

Links:

https://fernlotyards.com.au?bypass=farm

https://www.filecrate.example/sh/qrwpx8m3vd452kt/BBBDmwkqwwCqUbmKjAZ7OH-7b?dl=0

Target Market(s)

Primarily females aged 19 - 65 who work for a strata management and/or a property management company. These organisations oversee the maintenance aspects for apartments/condominiums and manage the properties on behalf of the owners.
The business that the website represents provides professional gardening services for commercial businesses and these apartment/condominium communities. So do not think home gardens and that type of gardening. Think on a larger scale like commercial businesses, hospitals, blocks of units/apartments/condominiums, shopping centres.

Industry/Entity Type

Commercial

Coding

Coded - Design and coding required

Number of Pages Required

5+ page

Requirements
Must have
• A great layout with lots of white space, intuitive navigation, prominent calls to action and professional looking.

The website needs to give the impression that the business is mid-size with a number of employees i.e. 6-10, yet still have the impression that it is a business where the owner is involved and there is a high level of personalised customer service.
Nice to have
• Maybe a looping video on the home page that is faded in the background that represents what the business does and who it services.
Should not have
• An attitude by the designer that anything will satisfy me. I want the designer to create a design that they would be proud to present to the market.

I have had too many bad experiences with website designers who do not have the appropriate attitude or skills to produce a quality site that appeals to me.

```html
<!DOCTYPE html>
<html lang="en">
<head>
<meta charset="utf-8">
<title>Fernlot Yards — Garden Care &amp; Maintenance</title>
<link rel="stylesheet" href="https://fonts.googleapis.com/css2?family=Marcellus&family=Mulish:wght@400;600;700;800&display=swap">
<style>
  :root{
    --green:#66b12f;
    --green-dark:#4f8f22;
    --slate:#566060;
    --slate-dark:#464e4e;
    --mint:#f3faec;
    --mint-2:#e6f4d9;
    --ink:#1f2323;
    --muted:#6d7373;
    --white:#ffffff;
    --line:#e4e8e4;
  }
  *{box-sizing:border-box;margin:0;padding:0}
  html,body{width:1200px;height:4043px;overflow:hidden;background:var(--white)}
  body{font-family:'Mulish',sans-serif;color:var(--ink);position:relative}
  .page{position:relative;width:1200px;height:4043px;overflow:hidden}
  .abs{position:absolute}
  .bands{position:absolute;left:0;top:0;width:1200px;height:4043px}

  /* header */
  .site-header{position:absolute;left:0;top:0;width:1200px;height:78px;background:var(--white);border-top:3px solid var(--green);box-shadow:0 1px 0 var(--line)}
  .brand{position:absolute;display:flex;align-items:center;gap:10px;font-family:'Mulish',sans-serif;font-weight:800;color:var(--green)}
  .brand-mark{background:var(--green);border-radius:3px}
  .header-brand{left:144px;top:20px;font-size:24px}
  .header-brand .brand-mark{width:32px;height:32px}
  .main-nav a{position:absolute;top:0;height:75px;line-height:75px;font-size:14px;color:var(--slate-dark);text-decoration:none}
  .main-nav a.active{background:var(--green);color:var(--white);width:56px;text-align:center}
  .header-phone{position:absolute;left:795px;top:24px;display:flex;align-items:center;gap:8px;font-weight:800;font-size:18px;color:var(--slate-dark)}
  .pill{display:inline-flex;align-items:center;justify-content:center;gap:8px;border-radius:30px;background:var(--slate);color:var(--white);font-weight:700;text-transform:uppercase;text-decoration:none}
  .btn-quote{position:absolute;left:952px;top:20px;width:104px;height:33px;font-size:11px}
  .arrow{display:inline-block;width:13px;height:13px;border-radius:50%;background:var(--white);position:relative}
  .arrow::after{content:"";position:absolute;left:4px;top:3.5px;border-left:5px solid var(--slate);border-top:3px solid transparent;border-bottom:3px solid transparent}

  /* hero */
  .hero-photo{position:absolute;left:0;top:78px;width:1200px;height:670px;background:linear-gradient(180deg,#3b4a2a 0%,#4e6a2e 45%,#5f8a30 75%,#7a6a4e 100%)}
  .hero-box{position:absolute;left:144px;top:193px;width:557px;height:317px;background:rgba(30,34,28,.55);padding:26px 56px}
  .hero-title{font-family:'Marcellus',serif;font-size:36px;line-height:48px;color:var(--white);font-weight:400;letter-spacing:.5px}
  .hero-title .accent{color:var(--green)}
  .hero-sub{margin-top:12px;font-size:17px;color:var(--white)}
  .btn-hero{margin-top:30px;width:166px;height:46px;font-size:13px}
  .dots{position:absolute;left:563px;top:620px;display:flex;gap:7px}
  .dots span{width:9px;height:9px;border-radius:50%;background:var(--white)}
  .dots span.on{background:var(--green)}

  /* headings */
  .section-title{font-family:'Marcellus',serif;font-weight:400;font-size:35px;color:var(--ink);letter-spacing:.5px}
  .section-title .accent{color:var(--green)}
  .rule{display:block;width:42px;height:3px;background:var(--green)}
  .centered{position:absolute;left:0;width:1200px;text-align:center}
  .centered .rule{margin:14px auto 0}

  /* welcome */
  .welcome-art{position:absolute;left:144px;top:790px;width:410px;height:410px;border-radius:6px;background:linear-gradient(135deg,var(--green) 0%,#8bc85a 45%,#8a8f8f 55%,#5f6565 100%);display:flex;align-items:center;justify-content:center}
  .welcome-art span{font-weight:800;font-size:34px;color:var(--white)}
  .welcome{position:absolute;left:588px;top:790px;width:470px}
  .welcome .rule{margin-top:14px}
  .welcome p{margin-top:34px;font-size:13px;line-height:26.5px;color:var(--muted)}
  .welcome p + p{margin-top:0}
  .btn-read{margin-top:30px;width:150px;height:46px;font-size:13px}

  /* services */
  .services-intro{position:absolute;left:0;width:1200px;top:1500px;text-align:center;font-size:13px;line-height:24px;color:var(--muted)}
  .service{position:absolute;top:1611px;width:240px;text-align:center}
  .service-photo{width:200px;height:200px;margin:0 auto;border-radius:50%;border:4px solid var(--green-dark);padding:6px;background:var(--white)}
  .service-photo div{width:100%;height:100%;border-radius:50%}
  .service h3{margin-top:28px;font-size:17px;line-height:23px;font-weight:700;color:var(--ink)}
  .service p{margin-top:12px;font-size:12px;line-height:22.5px;color:var(--muted)}
  .btn-small{margin-top:14px;width:116px;height:33px;font-size:11px}

  /* work */
  .work-grid{position:absolute;left:144px;top:2361px;width:912px;display:grid;grid-template-columns:repeat(3,300px);grid-auto-rows:281px;gap:7px 6px}
  .btn-more{position:absolute;left:524px;top:2974px;width:152px;height:44px;font-size:13px}

  /* contact */
  .contact-bg{position:absolute;left:0;top:3082px;width:1200px;height:754px}
  .contact-title{color:var(--white)}
  .contact-title + .rule{background:var(--white)}
  .field{position:absolute;background:var(--white);font-size:13px;color:#555;padding:0 22px;display:flex;align-items:center}
  .btn-submit{position:absolute;left:501px;top:3631px;width:198px;height:44px;font-size:13px}

  /* footer */
  .footer-brand{left:160px;top:3900px;font-size:30px}
  .footer-brand .brand-mark{width:40px;height:40px}
  .footer-phone{position:absolute;left:610px;top:3912px;display:flex;align-items:center;gap:10px;font-weight:800;font-size:24px;color:var(--ink)}
  .social{position:absolute;left:836px;top:3909px;display:flex;gap:8px}
  .social span{width:35px;height:35px;border-radius:50%;border:2px solid var(--green)}
  .copyright{position:absolute;left:152px;top:3985px;font-size:13px;color:var(--slate-dark)}
  .footer-nav a{position:absolute;top:3983px;font-size:18px;font-weight:600;color:var(--ink);text-decoration:none}
</style>
</head>
<body>
<div class="page">

  <!-- background bands -->
  <div class="hero-photo" role="img" aria-label="Photo of a freshly mowed lawn with trees and a brick-paved path"></div>
  <div class="hero-box">
    <h1 class="hero-title">SCHEDULED GARDEN CARE<br><span class="accent">PROGRAMS AND GARDEN</span><br>MAINTENANCE SERVICE</h1>
    <p class="hero-sub">for residential, strata and commercial properties</p>
    <a class="pill btn-hero" href="#">Get Started <i class="arrow"></i></a>
  </div>
  <div class="dots"><span></span><span></span><span class="on"></span><span></span><span></span></div>

  <div class="contact-bg" role="img" aria-label="Green-tinted photo of a park bench on a lawn" style="background:linear-gradient(180deg,#5fae2a 0%,#6cbf34 50%,#5ea62c 100%)"></div>

  <svg class="bands" viewBox="0 0 1200 4043" aria-hidden="true">
    <!-- hero bottom chevron -->
    <polygon points="0,565 600,728 1200,565 1200,600 600,748 0,600" fill="#566060"/>
    <polygon points="0,600 600,748 1200,600 1200,770 0,770" fill="#ffffff"/>
    <!-- services band -->
    <polygon points="0,1396 361,1247 839,1247 1200,1396 1200,2034 839,2181 361,2181 0,2034" fill="#f3faec"/>
    <polygon points="600,1290 839,1247 1200,1396" fill="#e6f4d9"/>
    <polygon points="0,2034 361,2181 420,2120" fill="#e6f4d9"/>
    <!-- contact band mask -->
    <polygon points="0,3082 361,3082 0,3232" fill="#ffffff"/>
    <polygon points="839,3082 1200,3082 1200,3232" fill="#ffffff"/>
    <polygon points="0,3687 361,3836 0,3836" fill="#ffffff"/>
    <polygon points="1200,3687 839,3836 1200,3836" fill="#ffffff"/>
    <polygon points="0,3232 361,3082 600,3125" fill="#566060"/>
    <polygon points="839,3836 1200,3687 1200,3712" fill="#566060"/>
  </svg>

  <!-- header -->
  <header class="site-header">
    <div class="brand header-brand"><span class="brand-mark"></span>Fernlot Yards</div>
    <nav class="main-nav">
      <a class="active" href="#" style="left:449px">Home</a>
      <a href="#" style="left:519px">About</a>
      <a href="#" style="left:578px">Services</a>
      <a href="#" style="left:653px">Work</a>
      <a href="#" style="left:708px">Contact</a>
    </nav>
    <div class="header-phone">
      <svg width="24" height="24" viewBox="0 0 24 24" aria-hidden="true"><circle cx="12" cy="12" r="10.5" fill="none" stroke="#66b12f" stroke-width="2"/><path d="M8.5 7c.5-.4 1.2-.3 1.5.2l1 1.6c.3.5.2 1-.2 1.4l-.6.5c.6 1.3 1.6 2.3 2.9 2.9l.5-.6c.4-.4.9-.5 1.4-.2l1.6 1c.5.3.6 1 .2 1.5l-.6.7c-.7.8-2 .9-3.4.2-2.4-1.2-4.3-3.1-5.5-5.5-.7-1.4-.6-2.7.2-3.4z" fill="#66b12f"/></svg>
      0400 555 182
    </div>
    <a class="pill btn-quote" href="#">Free Quote</a>
  </header>

  <!-- welcome -->
  <div class="welcome-art"><span>Fernlot Yards</span></div>
  <section class="welcome">
    <h2 class="section-title">WELCOME TO <span class="accent">FERNLOT YARDS</span></h2>
    <span class="rule"></span>
    <p>Fernlot Yards is a privately owned Perth based garden care and maintenance business. Fernlot Yards provides both one-off garden maintenance as well as scheduled garden care programs for residential, strata and commercial properties in most areas of the Perth metropolitan area.</p>
    <p>We have the resources of highly talented hands-on landscape designers, horticulturalists, reticulation installers and turf experts available and we can purchase plants and products at wholesale prices.</p>
    <a class="pill btn-read" href="#">Read More <i class="arrow"></i></a>
  </section>

  <!-- services -->
  <div class="centered" style="top:1408px">
    <h2 class="section-title">OUR <span class="accent">SERVICES</span></h2>
    <span class="rule"></span>
  </div>
  <p class="services-intro">Fernlot Yards provides a full complement of garden services for residential, strata and commercial properties.<br>Our four key gardening services are</p>

  <article class="service" style="left:106px">
    <div class="service-photo"><div role="img" aria-label="Photo of a cleared garden bed being prepared" style="background:linear-gradient(180deg,#cfe0ee 0%,#8a7a62 55%,#6a5a45 100%)"></div></div>
    <h3>Scheduled Garden<br>Care Program</h3>
    <p>Our Garden Care Program is<br>tailored to have your garden<br>look good all year</p>
    <a class="pill btn-small" href="#">Read More <i class="arrow"></i></a>
  </article>
  <article class="service" style="left:355px">
    <div class="service-photo"><div role="img" aria-label="Photo of a maintained garden with trees and lawn" style="background:linear-gradient(180deg,#c8d8d0 0%,#4e6a34 45%,#6e8c3a 100%)"></div></div>
    <h3>Garden Maintenance<br>Services</h3>
    <p>Our Garden Maintenance Services<br>are once off attendances<br>when required</p>
    <a class="pill btn-small" href="#">Read More <i class="arrow"></i></a>
  </article>
  <article class="service" style="left:605px">
    <div class="service-photo"><div role="img" aria-label="Photo of a sprinkler watering a lawn" style="background:linear-gradient(180deg,#9fcf5a 0%,#5e9a2a 55%,#3e6a1e 100%)"></div></div>
    <h3>Reticulation<br>Services</h3>
    <p>Our Reticulation Service covers<br>all aspects of garden and<br>lawn irrigation</p>
    <a class="pill btn-small" href="#">Read More <i class="arrow"></i></a>
  </article>
  <article class="service" style="left:853px">
    <div class="service-photo"><div role="img" aria-label="Photo of a modern house with a front garden" style="background:linear-gradient(180deg,#4a8ad8 0%,#9cc2ec 40%,#6a6e70 60%,#c8c8c0 100%)"></div></div>
    <h3>Specialty<br>Garden Services</h3>
    <p>Our Specialty Garden Services are<br>designed to address specific<br>issues in your garden</p>
    <a class="pill btn-small" href="#">Read More <i class="arrow"></i></a>
  </article>

  <!-- work -->
  <div class="centered" style="top:2247px">
    <h2 class="section-title">OUR <span class="accent">WORK</span></h2>
    <span class="rule"></span>
  </div>
  <div class="work-grid">
    <div role="img" aria-label="Photo of an open grassy block" style="background:linear-gradient(180deg,#dcdcd8 0%,#8e9a6a 40%,#9a9468 100%)"></div>
    <div role="img" aria-label="Photo of an overgrown garden beside a wall" style="background:linear-gradient(180deg,#4a5a3a 0%,#3e6a28 50%,#2e4a22 100%)"></div>
    <div role="img" aria-label="Photo of a garden with a brick pillar and shrubs" style="background:linear-gradient(180deg,#5a7040 0%,#6a5a40 55%,#8a7a5a 100%)"></div>
    <div role="img" aria-label="Photo of a paved path through a dry garden" style="background:linear-gradient(180deg,#6a7a4a 0%,#8a6a52 50%,#a08a70 100%)"></div>
    <div role="img" aria-label="Photo of a garden bed with new plant supports" style="background:linear-gradient(180deg,#5a6a4a 0%,#6a5a48 50%,#7a6a55 100%)"></div>
    <div role="img" aria-label="Photo of a roadside verge beside a commercial building" style="background:linear-gradient(180deg,#5a9ae0 0%,#b6cfe6 40%,#9a9a8a 65%,#6a6a58 100%)"></div>
  </div>
  <a class="pill btn-more" href="#">View More <i class="arrow"></i></a>

  <!-- contact -->
  <div class="centered" style="top:3236px">
    <h2 class="section-title contact-title">CONTACT FORM</h2>
    <span class="rule"></span>
  </div>
  <div class="field" style="left:234px;top:3352px;width:359px;height:52px">First Name</div>
  <div class="field" style="left:605px;top:3352px;width:360px;height:52px">Last Name</div>
  <div class="field" style="left:234px;top:3416px;width:359px;height:52px">Email address</div>
  <div class="field" style="left:605px;top:3416px;width:360px;height:52px">Phone Number</div>
  <div class="field" style="left:234px;top:3482px;width:731px;height:113px;align-items:flex-start;padding-top:18px">Message</div>
  <a class="pill btn-submit" href="#">Submit Message <i class="arrow"></i></a>

  <!-- footer -->
  <footer>
    <div class="brand footer-brand"><span class="brand-mark"></span>Fernlot Yards</div>
    <div class="footer-phone">
      <svg width="34" height="34" viewBox="0 0 24 24" aria-hidden="true"><circle cx="12" cy="12" r="10.5" fill="none" stroke="#66b12f" stroke-width="1.6"/><path d="M8.5 7c.5-.4 1.2-.3 1.5.2l1 1.6c.3.5.2 1-.2 1.4l-.6.5c.6 1.3 1.6 2.3 2.9 2.9l.5-.6c.4-.4.9-.5 1.4-.2l1.6 1c.5.3.6 1 .2 1.5l-.6.7c-.7.8-2 .9-3.4.2-2.4-1.2-4.3-3.1-5.5-5.5-.7-1.4-.6-2.7.2-3.4z" fill="#66b12f"/></svg>
      0400 555 182
    </div>
    <div class="social" aria-label="Social links"><span></span><span></span><span></span><span></span></div>
    <p class="copyright">© 2020 fernlotyards. All rights reserved &nbsp;|&nbsp; Privacy &nbsp;|&nbsp; Terms of Use</p>
    <nav class="footer-nav">
      <a href="#" style="left:610px">HOME</a>
      <a href="#" style="left:686px">ABOUT</a>
      <a href="#" style="left:773px">SERVICES</a>
      <a href="#" style="left:883px">WORK</a>
      <a href="#" style="left:964px">CONTACT</a>
    </nav>
  </footer>

</div>
</body>
</html>
```